Business card for consulting firm

We need a double-sided business card for consulting firm, VantorQ. The card should be professional but also creative and visually interesting.

Target Market(s)

Engineering and technology; transport industries; safety critical / heavy industry.

Contact Information for Business Card

See attached file with details.

Font styles to use
Sans Serif

```html
<!DOCTYPE html>
<html lang="en">
<head>
<meta charset="utf-8">
<title>VantorQ Business Card</title>
<link rel="stylesheet" href="https://fonts.googleapis.com/css2?family=Open+Sans:wght@400;600;700&display=swap">
<style>
  :root {
    --page-bg: #ecebe8;
    --card-white: #ffffff;
    --brand-blue: #1ab6e6;
    --brand-navy: #1b2a3f;
    --text-dark: #2a2a2a;
    --card-shadow: rgba(0, 0, 0, 0.28);
  }
  * { margin: 0; padding: 0; box-sizing: border-box; }
  html, body {
    width: 1200px;
    height: 900px;
    overflow: hidden;
    background: var(--page-bg);
    font-family: "Open Sans", Arial, sans-serif;
  }
  .card {
    position: absolute;
    left: 320px;
    width: 582px;
    height: 358px;
    border-radius: 18px;
    box-shadow: 3px 4px 6px var(--card-shadow);
  }
  .card--front { top: 88px; background: var(--card-white); }
  .card--back { top: 478px; background: var(--brand-blue); }

  .wordmark {
    position: absolute;
    font-weight: 700;
    color: var(--brand-navy);
    letter-spacing: 1px;
    line-height: 1;
  }
  .tagline {
    position: absolute;
    color: var(--brand-navy);
    font-weight: 400;
    line-height: 1;
  }
  .card--front .wordmark { left: 34px; top: 154px; font-size: 38px; }
  .card--front .tagline { left: 92px; top: 191px; font-size: 13px; }

  .card--back .wordmark { left: 0; width: 100%; text-align: center; top: 152px; font-size: 62px; letter-spacing: 2px; }
  .card--back .tagline { left: 203px; top: 216px; font-size: 19px; }

  .contact {
    position: absolute;
    left: 288px;
    top: 94px;
    color: var(--text-dark);
  }
  .contact__name {
    font-size: 19px;
    font-weight: 600;
    color: var(--brand-blue);
    line-height: 22px;
  }
  .contact__quals { font-size: 12.5px; line-height: 20px; }
  .contact__role { font-size: 15.5px; line-height: 22px; }
  .contact__list { list-style: none; margin-top: 20px; }
  .contact__item {
    display: flex;
    align-items: center;
    gap: 5px;
    font-size: 15px;
    line-height: 21px;
  }
  .contact__icon { width: 12px; height: 12px; flex: none; fill: var(--brand-blue); }
</style>
</head>
<body>
  <section class="card card--front">
    <div class="wordmark">VANTORQ</div>
    <div class="tagline">Safety &amp; Human Factors</div>

    <div class="contact">
      <div class="contact__name">HARRIET KELLAWAY</div>
      <div class="contact__quals">BA (Hons), M Psych Org, M Tech Mgt (HF)</div>
      <div class="contact__role">Managing Director</div>
      <ul class="contact__list">
        <li class="contact__item">
          <svg class="contact__icon" viewBox="0 0 12 12" aria-hidden="true"><path d="M1 4.5C1 3 3 2 6 2s5 1 5 2.5L9 5.5 8.5 4h-5L3 5.5zM3 6h6l1.5 4.5h-9z"/></svg>
          +61 (0)400 555 014
        </li>
        <li class="contact__item">
          <svg class="contact__icon" viewBox="0 0 12 12" aria-hidden="true"><path d="M1 3h10v6H1z"/><path d="M1 3l5 3.5L11 3" fill="none" stroke="#fff" stroke-width="1"/></svg>
          hkellaway@vantorq.com.au
        </li>
        <li class="contact__item">
          <svg class="contact__icon" viewBox="0 0 12 12" aria-hidden="true"><circle cx="6" cy="6" r="5.5"/><path d="M3 4.5c1 0 2 1 1.5 2S6 8 5.5 10M7.5 2c0 1.5 1.5 1.5 2.5 2.5" fill="none" stroke="#fff" stroke-width="1"/></svg>
          www.vantorq.global
        </li>
        <li class="contact__item">
          <svg class="contact__icon" viewBox="0 0 12 12" aria-hidden="true"><circle cx="6" cy="6" r="5.5"/><path d="M3 4.5c1 0 2 1 1.5 2S6 8 5.5 10M7.5 2c0 1.5 1.5 1.5 2.5 2.5" fill="none" stroke="#fff" stroke-width="1"/></svg>
          www.vantorq.com.au
        </li>
      </ul>
    </div>
  </section>

  <section class="card card--back">
    <div class="wordmark">VANTORQ</div>
    <div class="tagline">Safety &amp; Human Factors</div>
  </section>
</body>
</html>
```